ThisIsRayWendt.com needs a modern, eye-catching business card design

My name is Ray Wendt and I own a video training (software development industry) website. I need a business card design that is eye catching for when I travel to conferences or do seminars. I would prefer something simple but bold. Something along the lines of this: https://pixvaultcdn.example/design_img/512376/40918/40918_7720341_512376_image.jpg

Note that I do not have a specific logo, but I do have an caricature I use on my site of myself. I've not attached it because I'm not really a fan of having it on my business cards. I would prefer lettering instead of an image. You can go to my website (https://thisisraywendt.example) for inspiration.

I want to add the following information on my card (the order of these, their size, and their casing is up to you):

Ray Wendt
ray@ThisIsRayWendt.example
@ThisIsRayWendt
ThisIsRayWendt.com
vidstream.example/ThisIsRayWendt

I would also like to have somewhere on the card a small ad that says "Get a free course at https://ThisIsRayWendt.example/FreeCourse". Feel free to play with that wording or layout if you need. I would prefer this text to be at the bottom of the card and subtle. Some small eye-catching thing might be ok but nothing huge or garish.

I plan on printing this card at prixa.example (https://www.prixa.example/us/design-guidelines/business-cards.html). I would like it to be the standard size (3.66" x 2.16"). I would prefer rounded corners and horizontal orientation. This is a two-side design. I would prefer the side with all of the information be primarily white but I like color text (again, flexible on that). On the front side, I like simple. Maybe just ThisIsRayWendt.com (casing on that is up to you - whatever looks and reads the best - that goes for all of the casing). As for font choices, I prefer a modern, clean font. For example, Open Sans Light can be a nice option.

Website Info (might be helpful for the card):
Color Palette

Darkest blue - #263246
Alternate blue - #2F4E6A
Light blue - #2A98C3
Orange - #FF6201
White - #FFFFFF

Font for Ray Wendt Logo

Jellyka Estryas Handwriting
http://www.typeharborfree.example/jellyka_estryas_handwriting.font

Fonts for Site Content and VidStream Thumbnails

Lovelo (bold title font)
http://www.glyphmill.example/lovelo-font/

Open Sans (body font)
http://www.letterburrow.example/fonts/open-sans

Industry/Entity Type

Software Development

Contact Information for Business Card

Ray Wendt
ray@ThisIsRayWendt.example
@ThisIsRayWendt
ThisIsRayWendt.com
vidstream.example/ThisIsRayWendt

Get a free course at https://ThisIsRayWendt.example/FreeCourse

Colors

Designer to choose colors to be used in the design.

Requirements
Nice to have
• Modern color - maybe primarily a color on the front and then that color as an accent on the back.
Should not have
• Lots of colors - I LOVE color but do not want a rainbow of colors on the card.

```html
<!DOCTYPE html>
<html lang="en">
<head>
<meta charset="utf-8">
<title>Ray Wendt — Business Cards</title>
<link href="https://fonts.googleapis.com/css2?family=Open+Sans:wght@300;400;600;700&family=Josefin+Sans:wght@700&family=Nothing+You+Could+Do&display=swap" rel="stylesheet">
<style>
  :root {
    --navy: #263246;
    --alt-blue: #2F4E6A;
    --light-blue: #2A98C3;
    --orange: #FF6201;
    --white: #FFFFFF;
    --ink: #2b3445;
    --stage: #e9e6e2;
    --portrait-skin: #c98a62;
    --portrait-shirt: #3f6f85;
  }
  * { box-sizing: border-box; margin: 0; padding: 0; }
  html, body { width: 1200px; height: 891px; overflow: hidden; }
  body {
    background: var(--stage);
    font-family: "Open Sans", Arial, sans-serif;
    position: relative;
  }
  .card {
    position: absolute;
    width: 560px;
    height: 331px;
    border-radius: 14px;
    overflow: hidden;
    background: var(--white);
    box-shadow: 0 8px 24px rgba(0,0,0,.14);
  }
  .card--front { left: 610px; top: 280px; }
  .card--back { left: 30px; top: 280px; }

  .portrait {
    position: absolute;
    border-radius: 40% 40% 18% 18%;
    background: linear-gradient(180deg, var(--portrait-skin) 0 58%, var(--portrait-shirt) 58% 100%);
  }

  /* Front (white) card */
  .card--front .portrait { left: 190px; top: 118px; width: 74px; height: 80px; }
  .front-name {
    position: absolute; left: 280px; top: 120px;
    font-family: "Nothing You Could Do", cursive;
    font-size: 38px; line-height: 1; letter-spacing: 2px;
  }
  .front-name .first { color: var(--navy); }
  .front-name .last { color: var(--orange); margin-left: 14px; }
  .front-role {
    position: absolute; left: 292px; top: 178px;
    font-size: 11px; font-weight: 600; color: var(--ink);
  }
  .front-rule {
    position: absolute; left: 0; top: 246px; width: 230px; height: 3px;
    background: var(--orange);
  }
  .front-band {
    position: absolute; left: 0; top: 262px; width: 100%; height: 26px;
    background: var(--orange);
    display: flex; align-items: center;
    font-size: 10.5px; color: var(--navy); font-weight: 600;
  }
  .front-band .site { width: 220px; padding-left: 30px; letter-spacing: 1px; }
  .front-band .divider { width: 8px; height: 26px; border-left: 3px solid var(--navy); border-right: 3px solid var(--navy); background: var(--orange); }
  .front-band .ad { flex: 1; text-align: right; padding-right: 26px; }
  .front-band .ad b { font-weight: 700; }

  /* Back (navy/white) card */
  .back-top {
    position: absolute; left: 0; top: 0; width: 100%; height: 150px;
    background: var(--navy);
    border-bottom: 3px solid var(--orange);
  }
  .card--back .portrait { left: 150px; top: 30px; width: 76px; height: 84px; }
  .back-name {
    position: absolute; left: 250px; top: 52px;
    font-family: "Nothing You Could Do", cursive;
    font-size: 42px; color: var(--white); letter-spacing: 3px; line-height: 1;
  }
  .back-title {
    position: absolute; left: 34px; top: 178px;
    font-family: "Josefin Sans", sans-serif; font-weight: 700;
    font-size: 22px; letter-spacing: 6px; color: var(--navy);
  }
  .back-role {
    position: absolute; left: 36px; top: 208px;
    font-size: 10px; color: var(--ink);
  }
  .back-divider {
    position: absolute; left: 268px; top: 178px; width: 1.5px; height: 52px;
    background: var(--navy);
  }
  .contacts {
    position: absolute; left: 294px; top: 172px;
    list-style: none; font-size: 11px; color: var(--ink);
  }
  .contacts li { display: flex; align-items: center; gap: 9px; height: 21px; }
  .contacts svg { width: 15px; height: 15px; flex: none; }
  .ad-tab {
    position: absolute; left: 70px; top: 258px; width: 250px; height: 60px;
    background: var(--navy);
    clip-path: polygon(16px 0, 100% 0, 100% 100%, 0 100%, 0 16px);
    color: var(--white); text-align: center;
    font-size: 10.5px; padding-top: 12px; line-height: 1.5;
  }
  .back-bottom-rule {
    position: absolute; left: 0; top: 318px; width: 100%; height: 3px;
    background: var(--orange);
  }
</style>
</head>
<body>

  <section class="card card--front" aria-label="Business card, white side">
    <div class="portrait" role="img" aria-label="Caricature portrait of Ray Wendt"></div>
    <div class="front-name"><span class="first">Ray</span><span class="last">Wendt</span></div>
    <div class="front-role">Software Development</div>
    <div class="front-rule"></div>
    <div class="front-band">
      <span class="site">www.thisisraywendt.example</span>
      <span class="divider"></span>
      <span class="ad"><b>Get a free course at</b> www.thisisraywendt.example/FreeCourse</span>
    </div>
  </section>

  <section class="card card--back" aria-label="Business card, contact side">
    <div class="back-top"></div>
    <div class="portrait" role="img" aria-label="Caricature portrait of Ray Wendt"></div>
    <div class="back-name">Ray Wendt</div>
    <div class="back-title">RAY WENDT</div>
    <div class="back-role">Software Development</div>
    <div class="back-divider"></div>
    <ul class="contacts">
      <li>
        <svg viewBox="0 0 16 16" aria-hidden="true"><circle cx="8" cy="8" r="8" fill="var(--navy)"/></svg>
        vidstream.example/ThisIsRayWendt
      </li>
      <li>
        <svg viewBox="0 0 16 16" aria-hidden="true"><circle cx="8" cy="8" r="8" fill="var(--navy)"/><rect x="4" y="5" width="8" height="6" fill="none" stroke="#fff" stroke-width="1"/><path d="M4 5 L8 8.5 L12 5" fill="none" stroke="#fff" stroke-width="1"/></svg>
        ray@ThisIsRayWendt.example
      </li>
      <li>
        <svg viewBox="0 0 16 16" aria-hidden="true"><circle cx="8" cy="8" r="8" fill="var(--navy)"/><rect x="4" y="4.5" width="8" height="7" rx="1" fill="none" stroke="#fff" stroke-width="1"/><line x1="4" y1="6.5" x2="12" y2="6.5" stroke="#fff" stroke-width="1"/></svg>
        https://thisisraywendt.example
      </li>
    </ul>
    <div class="ad-tab">Get a free course at<br>https://ThisIsRayWendt.example/FreeCourse</div>
    <div class="back-bottom-rule"></div>
  </section>

</body>
</html>
```